Mirela Hastow ADHD coach needs a flyer

I need a flyer to be sent by email. the copy is attached. It can be changed/reduced to fit the flyer. I would like to keep my website colors. My website is www.mirelahastow.example - Thank you!

```html
<!DOCTYPE html>
<html lang="en">
<head>
<meta charset="utf-8">
<title>Mirela Hastow – Academic Success Coaching</title>
<link rel="stylesheet" href="https://fonts.googleapis.com/css2?family=Montserrat:wght@700;800&family=Open+Sans:ital,wght@0,400;0,600;0,700;1,700&display=swap">
<style>
:root{
  --accent:#88a9b8;
  --teal-dark:#4e6f78;
  --ink:#26252b;
  --slate:#5e5f63;
  --panel-a:#9ca7aa;
  --panel-b:#8e9da2;
  --quote-band:#5c5c5e;
  --text:#2b2b2b;
  --white:#ffffff;
}
*{margin:0;padding:0;box-sizing:border-box}
html,body{width:788px;height:1200px;overflow:hidden;background:var(--white)}
.flyer{position:relative;width:788px;height:1200px;font-family:"Open Sans",Arial,sans-serif;color:var(--text)}
.shapes{position:absolute;inset:0}
.headline{position:absolute;left:63px;top:26px;width:660px;font-family:"Montserrat",Arial,sans-serif;font-weight:800;font-size:33.5px;line-height:34.5px;color:var(--accent)}
.site{position:absolute;left:70px;top:178px;font-family:"Open Sans",Arial,sans-serif;font-weight:700;font-size:20px;color:var(--white)}
.portrait{position:absolute;left:466px;top:205px;width:322px;height:395px;background:radial-gradient(ellipse at 55% 35%,#e3d4cf 0%,#d9c9c9 30%,#9aa6aa 72%,#8e9da2 100%)}
.tagline{position:absolute;left:61px;top:253px;width:490px;font-weight:700;font-style:italic;font-size:17px;line-height:21px;color:var(--white)}
.intro{position:absolute;left:61px;top:337px;width:390px;font-size:11.4px;line-height:14.6px;color:var(--white)}
.intro p+p{margin-top:14px}
.nameplate{position:absolute;left:520px;top:594px;width:225px;text-align:center;color:var(--white)}
.nameplate .name{font-family:"Montserrat",Arial,sans-serif;font-weight:800;font-size:20px;letter-spacing:.3px}
.nameplate .role{font-size:11.5px;font-weight:600;margin-top:4px}
.section-title{font-family:"Montserrat",Arial,sans-serif;font-weight:800;font-size:21px;color:var(--accent);line-height:24px}
.section-sub{font-weight:700;font-size:14.5px;color:var(--accent);line-height:18px}
.list-title{font-weight:700;font-size:13.4px;color:var(--accent)}
.helps{position:absolute;left:54px;top:645px;width:360px}
.helps .lead{margin-top:14px;font-size:11.3px;line-height:14px;padding-left:1px}
.helps .list-title{margin-top:9px}
.tri-list{list-style:none;margin-top:6px}
.tri-list li{position:relative;padding-left:12px;font-size:11.3px;line-height:14px;margin-bottom:5px}
.tri-list li::before{content:"";position:absolute;left:0;top:3px;border-left:6px solid var(--accent);border-top:4px solid transparent;border-bottom:4px solid transparent}
.potential{position:absolute;left:444px;top:714px;width:330px}
.potential .section-sub{margin-top:4px}
.sq-list{list-style:none;margin-top:6px}
.sq-list li{position:relative;padding-left:11px;font-size:11.3px;line-height:17.6px}
.sq-list li::before{content:"";position:absolute;left:0;top:6px;width:4px;height:4px;background:var(--accent)}
.potential .list-title.have{margin-top:13px;font-size:15px}
.quotes{position:absolute;left:0;top:991px;width:788px;height:152px;background:var(--quote-band);color:#ececec}
.quote-col{position:absolute;top:10px}
.quote-col.parents{left:54px;width:300px}
.quote-col.students{left:386px;width:370px}
.quote-head{display:flex;align-items:center;gap:8px;font-family:"Montserrat",Arial,sans-serif;font-weight:700;font-size:12.2px;color:var(--white);margin-bottom:10px}
.quote-head::after{content:"";flex:1;height:1px;background:#bdbdbd}
.quote{font-size:11.1px;line-height:13.8px;margin-bottom:13px}
.quote b{font-weight:700;color:var(--white)}
.next-label{position:absolute;left:66px;top:1152px;font-family:"Montserrat",Arial,sans-serif;font-weight:800;font-size:22px;color:var(--accent);letter-spacing:.5px}
.next-arrows{position:absolute;left:215px;top:1148px}
.next-cta{position:absolute;left:296px;top:1151px;font-family:"Montserrat",Arial,sans-serif;font-weight:700;font-size:14px;line-height:18px;color:#58585a}
</style>
</head>
<body>
<div class="flyer">
  <svg class="shapes" width="788" height="1200" viewBox="0 0 788 1200" aria-hidden="true">
    <defs>
      <linearGradient id="panelFill" x1="0" x2="1" y1="0" y2="0">
        <stop offset="0" stop-color="var(--panel-a)"/>
        <stop offset="1" stop-color="var(--panel-b)"/>
      </linearGradient>
    </defs>
    <rect x="0" y="199" width="788" height="420" fill="url(#panelFill)"/>
    <polygon points="0,150 436,150 542,122 605,200 455,200 352,234 0,234" fill="var(--ink)"/>
    <polygon points="436,150 542,122 456,208 380,208" fill="var(--slate)"/>
    <g fill="none" stroke="var(--accent)" stroke-width="1.6">
      <polyline points="628,149 641,165 628,181"/>
      <polyline points="641,149 654,165 641,181"/>
      <polyline points="654,149 667,165 654,181"/>
      <polyline points="667,149 680,165 667,181"/>
      <polyline points="680,149 693,165 680,181"/>
      <polyline points="693,149 706,165 693,181"/>
      <polyline points="706,149 719,165 706,181"/>
      <polyline points="719,149 732,165 719,181"/>
      <polyline points="732,149 745,165 732,181"/>
    </g>
  </svg>

  <h1 class="headline">Helping Your Child with ADHD or Other Learning Challenges Thrive in College and Beyond</h1>
  <div class="site">www.mirelahastow.example</div>

  <div class="portrait" role="img" aria-label="Portrait photo of Mirela Hastow in a pale pink blazer, arms crossed"></div>

  <svg class="shapes" width="788" height="1200" viewBox="0 0 788 1200" aria-hidden="true">
    <polygon points="285,619 420,619 335,688" fill="var(--accent)"/>
    <polygon points="414,605 492,605 409,688 335,688" fill="var(--teal-dark)"/>
    <polygon points="497,575 788,575 788,659 414,659" fill="var(--accent)"/>
  </svg>

  <p class="tagline">Academic success coaching that leads to lifelong transformation for students with ADHD and similar challenges that may have impeded their ability to thrive.</p>

  <div class="intro">
    <p>Sending your child off to college can feel scary, especially if that college is hundreds of miles away. You worry about how they’ll do on their own—whether they’ll make friends, earn good grades, and be happy—especially without you there to support them daily. You know your child is bright, and you want them to have a great future, but you’re concerned they will struggle without the right support and resources.</p>
    <p>You don’t need to feel helpless as you send your child off to this next stage of their lives. Mirela is dedicated to making that transition easier for everyone. Mirela Hastow has years of experience helping students thrive despite their challenges. She sees your child’s potential and helps them see it, too. She provides a safety net as they adjust to a new environment at college. Her services are comprehensive and adaptable, based on the requirements of each individual: helping with course selection and scheduling, time management, study strategies, focus, making new friends, and adapting to change. Through it all, Mirela guides students through fundamental work on mindset to ensure that changes stick.</p>
  </div>

  <div class="nameplate">
    <div class="name">MIRELA HASTOW</div>
    <div class="role">DESIGNATION HERE</div>
  </div>

  <section class="helps">
    <h2 class="section-title">Empowering Focus:</h2>
    <div class="section-sub">How Mirela Helps</div>
    <p class="lead">Mirela has taken students from failing to a 3.0 GPA, and from a C student to the Dean’s List, in just one semester. It doesn’t take years to provide lasting results; all it takes is the right guide.</p>
    <h3 class="list-title">Uniquely positioned to help your child, Mirela:</h3>
    <ul class="tri-list">
      <li>Tailors support so that your child improves focus and maximizes their potential in college and beyond.</li>
      <li>Understands your child’s unique needs - she sees the gifts that others often miss.</li>
      <li>Knows the academic landscape intimately, including the challenges faced by students with ADHD and other conditions.</li>
      <li>Helps with the logistics of scheduling in a way that most advisors can’t, enrolling students in the courses that best suit their learning style.</li>
      <li>Nurtures the brilliance in your bright child.</li>
      <li>Provides a balance between encouraging students and challenging them.</li>
    </ul>
  </section>

  <section class="potential">
    <h2 class="section-title">Realizing Potential:</h2>
    <div class="section-sub">The Transformation You’ll See in Your Child</div>
    <ul class="sq-list">
      <li>A mindset of self-belief and increased confidence.</li>
      <li>Higher grades and the drive to graduate.</li>
      <li>Social integration and making friends.</li>
      <li>Happiness and fulfilment.</li>
      <li>A deep sense of personal achievement and pride.</li>
    </ul>
    <h3 class="list-title have">You Will Have:</h3>
    <ul class="sq-list">
      <li>Less stress, knowing that your child is in good hands.</li>
      <li>Fewer sleepless nights worrying about your child.</li>
      <li>Confidence that they are receiving the right support.</li>
      <li>Joy and pride at seeing them do well.</li>
    </ul>
  </section>

  <section class="quotes">
    <div class="quote-col parents">
      <div class="quote-head">What Parents Say</div>
      <p class="quote">“Mirela was the glue that kept our daughter in college… as our daughter’s Academic Coach, [she] gave our daughter the ability to finish strong by empowering her with the skills needed to be successful.” -<b>Lorena</b></p>
      <p class="quote">“Mirela has always told my daughter not that she can succeed, but that she will succeed.”- <b>Margit</b></p>
    </div>
    <div class="quote-col students">
      <div class="quote-head">What Students Say</div>
      <p class="quote">“Last semester I completed all 16 hours and I had the highest GPA I’ve ever had!” <b>-Former student</b></p>
      <p class="quote">“Under her instruction, my grades began to improve. I ended up making the Dean’s List during my time at Brackenridge, and I was also inducted into Theta Rho Kappa. I am currently in my first year of law school at Halvorsen University, a top tier school.”<b>- Former student</b></p>
    </div>
  </section>

  <div class="next-label">NEXT STEPS</div>
  <svg class="next-arrows" width="62" height="36" viewBox="0 0 62 36" aria-hidden="true">
    <g fill="none" stroke="var(--accent)" stroke-width="1.6">
      <polyline points="2,2 14,18 2,34"/>
      <polyline points="16,2 28,18 16,34"/>
      <polyline points="30,2 42,18 30,34"/>
      <polyline points="44,2 56,18 44,34"/>
    </g>
  </svg>
  <p class="next-cta">To learn more and discuss your child’s individual needs,<br>call 555·014·2290 or email coach@mirelahastow.example</p>
</div>
</body>
</html>
```